CPA Firm Business Card
Halvorin, Bestwick & Pardue CPAs, LLC
Project: CPA Firm Business Card
CPA Firm Business Card - Financial Services
Creative Brief
Professional
Moss Brandley, CPA
2867 E. Sable Way, Suite 348 Tucson, AZ 85619
moss@quillledger.net
In addition to business cards design I would also like to see designs for letterheads, envelopes and fax cover sheets.

```html
<!DOCTYPE html>
<html lang="en">
<head>
<meta charset="utf-8">
<title>Halvorin, Bestwick &amp; Pardue CPAs, LLC – Business Card</title>
<link rel="stylesheet" href="https://fonts.googleapis.com/css2?family=Roboto+Condensed:wght@400;700&family=Roboto:wght@400;500&display=swap">
<style>
  :root {
    --maroon: #7d1518;
    --maroon-dark: #5e0e10;
    --paper: #ffffff;
    --paper-shade: #ececec;
    --ink: #4a4a4a;
    --ink-soft: #6b6b6b;
    --backdrop: #e9e6e2;
  }
  * { box-sizing: border-box; margin: 0; padding: 0; }
  html, body {
    width: 1200px; height: 900px; overflow: hidden;
    background: var(--backdrop);
  }
  .canvas {
    position: relative; width: 1200px; height: 900px;
  }
  .card {
    position: absolute; left: 110px; top: 170px;
    width: 980px; height: 560px;
    background: var(--maroon);
    border-radius: 6px;
    box-shadow: 0 14px 30px rgba(0,0,0,.18);
    overflow: hidden;
  }
  .panel-top {
    position: absolute; left: 26px; top: 26px; right: 26px; height: 250px;
    background: linear-gradient(180deg, var(--paper) 0%, var(--paper-shade) 100%);
    border-radius: 0 48px 0 0;
  }
  .firm-mark {
    position: absolute; left: 60px; top: 62px;
    display: flex; align-items: center; gap: 26px;
  }
  .firm-mark__square {
    width: 110px; height: 110px; background: var(--maroon);
  }
  .firm-mark__name {
    font-family: "Roboto Condensed", Arial, sans-serif;
    font-weight: 700; color: var(--ink);
    text-transform: uppercase; line-height: 1.02;
    font-size: 40px; letter-spacing: .5px;
  }
  .firm-mark__name span { display: block; }
  .firm-mark__name .firm-mark__suffix { font-size: 22px; text-align: right; margin-top: 4px; }
  .name-band {
    position: absolute; left: 26px; top: 290px;
    font-family: "Roboto Condensed", Arial, sans-serif;
    font-weight: 700; font-size: 30px; color: var(--paper);
    padding-left: 18px;
  }
  .panel-bottom {
    position: absolute; left: 26px; top: 346px; right: 26px; bottom: 26px;
    background: linear-gradient(180deg, var(--paper-shade) 0%, var(--paper) 25%);
    border-radius: 0 0 48px 0;
  }
  .contact-list {
    list-style: none; position: absolute; left: 34px; top: 26px;
    font-family: Roboto, Arial, sans-serif; font-size: 19px; color: var(--ink-soft);
  }
  .contact-list li { display: flex; align-items: flex-start; gap: 12px; margin-bottom: 8px; line-height: 26px; }
  .contact-list .icon { flex: none; width: 24px; height: 24px; margin-top: 1px; }
  .web-address {
    position: absolute; right: 40px; top: 40px;
    font-family: Roboto, Arial, sans-serif; font-weight: 500;
    font-size: 19px; letter-spacing: 3px; color: var(--maroon);
  }
</style>
</head>
<body>
<div class="canvas">
  <div class="card">
    <div class="panel-top">
      <div class="firm-mark">
        <div class="firm-mark__square"></div>
        <div class="firm-mark__name">
          <span>Halvorin,</span>
          <span>Bestwick &amp;</span>
          <span>Pardue</span>
          <span class="firm-mark__suffix">CPAs, LLC</span>
        </div>
      </div>
    </div>

    <div class="name-band">Moss Brandley, CPA</div>

    <div class="panel-bottom">
      <ul class="contact-list">
        <li>
          <svg class="icon" viewBox="0 0 24 24" aria-hidden="true"><circle cx="12" cy="12" r="12" fill="var(--maroon)"/><path d="M12 5a4.5 4.5 0 0 0-4.5 4.5C7.5 13 12 19 12 19s4.5-6 4.5-9.5A4.5 4.5 0 0 0 12 5zm0 6.2a1.7 1.7 0 1 1 0-3.4 1.7 1.7 0 0 1 0 3.4z" fill="#fff"/></svg>
          <span>2867 E. Sable Way, Suite 348<br>Tucson, AZ 85619</span>
        </li>
        <li>
          <svg class="icon" viewBox="0 0 24 24" aria-hidden="true"><circle cx="12" cy="12" r="12" fill="var(--maroon)"/><path d="M8.6 6.5l1.8-.4 1.1 2.6-1.3 1a7 7 0 0 0 3.9 3.9l1-1.3 2.6 1.1-.4 1.8c-.1.5-.6.8-1.1.8A9.8 9.8 0 0 1 7.8 7.6c0-.5.3-1 .8-1.1z" fill="#fff"/></svg>
          <span>520-471-3862</span>
        </li>
        <li>
          <svg class="icon" viewBox="0 0 24 24" aria-hidden="true"><circle cx="12" cy="12" r="12" fill="var(--maroon)"/><rect x="7" y="10" width="10" height="7" rx="1" fill="#fff"/><rect x="9" y="6" width="6" height="4" fill="#fff"/><rect x="9" y="12" width="6" height="1.4" fill="var(--maroon)"/></svg>
          <span>520-471-3863</span>
        </li>
        <li>
          <svg class="icon" viewBox="0 0 24 24" aria-hidden="true"><circle cx="12" cy="12" r="12" fill="var(--maroon)"/><rect x="6" y="8" width="12" height="8.5" rx="1" fill="#fff"/><path d="M6.5 8.6l5.5 4.2 5.5-4.2" fill="none" stroke="var(--maroon)" stroke-width="1.3"/></svg>
          <span>moss@quillledger.net</span>
        </li>
      </ul>
      <div class="web-address">www.QuillLedger.com</div>
    </div>
  </div>
</div>
</body>
</html>
```